Granite, Zinc and Clay Roofing LLC needs a new business card

I need a new business card because I have a new address.
I do slate copper and tile roofs. My webpage is: www.granitezincandclayroofing.example

```html
<!DOCTYPE html>
<html lang="en">
<head>
<meta charset="utf-8">
<title>Granite, Zinc and Clay Roofing – Business Card</title>
<link href="https://fonts.googleapis.com/css2?family=Hind:wght@400;500;600&display=swap" rel="stylesheet">
<style>
  :root {
    --bg: #d9d9d9;
    --card-white: #ffffff;
    --brand-blue: #4f9ecf;
    --ink: #0a0a0a;
    --text: #1d1d1d;
  }
  * { box-sizing: border-box; margin: 0; padding: 0; }
  html, body { width: 1200px; height: 1059px; overflow: hidden; }
  body {
    background: var(--bg);
    font-family: "Hind", sans-serif;
    position: relative;
  }
  .card {
    position: absolute;
    left: 255px;
    width: 690px;
    height: 392px;
    border-radius: 18px;
    overflow: hidden;
  }
  .card--front { top: 100px; background: var(--card-white); }
  .card--back { top: 538px; background: var(--brand-blue); }

  .front-brand {
    position: absolute;
    left: 38px;
    top: 150px;
    width: 260px;
    display: flex;
    align-items: center;
    gap: 10px;
  }
  .brand-mark {
    width: 16px; height: 16px;
    background: var(--brand-blue);
    flex: none;
  }
  .brand-name {
    font-weight: 600;
    color: var(--ink);
    line-height: 1.1;
  }
  .front-brand .brand-name { font-size: 21px; }

  .divider {
    position: absolute;
    left: 325px; top: 109px;
    width: 1px; height: 173px;
    background: var(--brand-blue);
  }
  .contact {
    position: absolute;
    left: 355px; top: 104px;
    color: var(--text);
  }
  .contact__name {
    font-size: 24px; font-weight: 600;
    color: var(--brand-blue);
    line-height: 28px;
  }
  .contact__role { font-size: 17px; line-height: 20px; }
  .contact__address { margin-top: 14px; font-size: 16px; line-height: 20px; }
  .contact__lines { margin-top: 12px; list-style: none; font-size: 15.5px; line-height: 23.5px; }
  .contact__lines li { display: flex; align-items: center; gap: 7px; }
  .contact__lines svg { width: 13px; height: 13px; flex: none; }

  .wave { position: absolute; left: 0; bottom: 0; width: 690px; height: 52px; }

  .back-brand {
    position: absolute;
    inset: 0;
    display: flex;
    flex-direction: column;
    align-items: center;
    justify-content: center;
    text-align: center;
  }
  .back-brand .brand-name { font-size: 46px; }
</style>
</head>
<body>
  <section class="card card--front">
    <div class="front-brand">
      <span class="brand-mark"></span>
      <span class="brand-name">Granite, Zinc and Clay Roofing</span>
    </div>

    <div class="divider"></div>

    <div class="contact">
      <h1 class="contact__name">Marek (Mark) Halden</h1>
      <p class="contact__role">Owner</p>
      <p class="contact__address">2870 Fernhill Rd<br>Linden Falls, OH 44000</p>
      <ul class="contact__lines">
        <li>
          <svg viewBox="0 0 16 16" aria-hidden="true"><path fill="#4f9ecf" d="M1 6c0-2 3-3 7-3s7 1 7 3v1h-3.5V5.5h-7V7H1zM4 8h8l2 6H2z"/></svg>
          (555) 014-2290
        </li>
        <li>
          <svg viewBox="0 0 16 16" aria-hidden="true"><rect x="1" y="3" width="14" height="10" rx="1" fill="#4f9ecf"/><path d="M1.5 4l6.5 5 6.5-5" stroke="#fff" stroke-width="1.4" fill="none"/></svg>
          info@granitezincandclayroofing.example
        </li>
        <li>
          <svg viewBox="0 0 16 16" aria-hidden="true"><circle cx="8" cy="8" r="7" fill="#4f9ecf"/><path d="M1 8h14M8 1c-3 3-3 11 0 14M8 1c3 3 3 11 0 14" stroke="#fff" stroke-width="1" fill="none"/></svg>
          www.granitezincandclayroofing.example
        </li>
      </ul>
    </div>

    <svg class="wave" viewBox="0 0 690 52" preserveAspectRatio="none" aria-hidden="true">
      <path d="M0 30 C80 -5 250 0 450 22 C560 33 640 35 690 0 L690 12 C640 30 560 30 450 28 C250 10 80 12 0 36 Z" fill="#0a0a0a"/>
      <path d="M0 46 C80 18 250 6 450 28 C560 38 640 36 690 18 L690 52 L0 52 Z" fill="#4f9ecf"/>
    </svg>
  </section>

  <section class="card card--back">
    <div class="back-brand">
      <span class="brand-name">Granite, Zinc and Clay<br>Roofing</span>
    </div>
  </section>
</body>
</html>
```